Start up in business consultancy needs a business card

We need the business card's layout (we have already the logo). Our business is concerned on consultancy services delivered to companies on the matter of sustainability. Business card should be enough essentials and professional style.

Side A with the following info:
logo + a space for the claim (still to identify) + website of the company

Side B with the following info:
Name of business card holder + title of the business card holder + address of the company + space for mobile number, phone number, fax number + e-mail of business card holder + graphic details around.

Target Market(s)

Business of any sector

Industry/Entity Type

Business Service

Contact Information for Business Card

Name of the company:
Pianoverde srl
Società Benefit

Address of the company:
Via Lucerna, 7
21047 - Saronno (VA)

Website:
www.pianoverde.it

Name of the BC' holder:
Luca Ferentino

Title:
Co-fondatore

Email:
luca@pianoverde.it

Mobile:
+39 348 915 2074
Phone:
+39 348 915 2074
Fax:
+39 348 915 2074

Font styles to use
Other font styles liked:
• new gothic

```html
<!DOCTYPE html>
<html lang="it">
<head>
<meta charset="UTF-8">
<title>Pianoverde – biglietto da visita</title>
<link href="https://fonts.googleapis.com/css2?family=Arimo:wght@400;700&family=Oswald:wght@500;600&display=swap" rel="stylesheet">
<style>
  :root {
    --brand-blue: #1766ae;
    --ink: #2a2a2a;
    --paper: #ffffff;
    --backdrop: #e9ebee;
    --faint-blue: #e6eef7;
  }
  * { margin: 0; padding: 0; box-sizing: border-box; }
  html, body { width: 1200px; height: 900px; overflow: hidden; }
  body {
    background: var(--backdrop);
    font-family: "Arimo", Arial, sans-serif;
    position: relative;
  }
  .card {
    position: absolute;
    left: 290px;
    width: 620px;
    height: 354px;
    background: var(--paper);
    border-radius: 24px;
    overflow: hidden;
    box-shadow: 0 6px 24px rgba(0,0,0,0.12);
  }
  .card--front { top: 70px; }
  .card--back { top: 476px; }

  /* Side A */
  .front-ring {
    position: absolute; left: -150px; top: 150px;
    width: 330px; height: 330px;
    border: 16px solid var(--faint-blue);
    border-radius: 50%;
  }
  .front-brand {
    position: absolute; left: 230px; top: 46px;
    display: flex; align-items: center; gap: 12px;
  }
  .brand-dot {
    width: 62px; height: 62px; border-radius: 50%;
    border: 4px solid var(--brand-blue);
  }
  .wordmark {
    font-family: "Arimo", Arial, sans-serif;
    font-weight: 700;
    color: var(--brand-blue);
    letter-spacing: -0.5px;
  }
  .front-brand .wordmark { font-size: 34px; }
  .benefit-tag {
    position: absolute; right: 62px; top: 122px;
    font-family: "Oswald", "Arial Narrow", sans-serif;
    font-weight: 600; font-size: 17px;
    color: var(--brand-blue); text-transform: uppercase; letter-spacing: 0.3px;
  }
  .claim-line {
    position: absolute; left: 110px; right: 60px;
    border-top: 2px dotted #333;
  }
  .claim-line--one { top: 172px; }
  .claim-line--two { top: 226px; left: 130px; right: 40px; }
  .front-web {
    position: absolute; left: 0; right: 0; bottom: 34px;
    text-align: center; font-size: 15px; color: var(--ink);
  }
  .front-web strong { color: var(--brand-blue); font-weight: 400; }

  /* Side B */
  .back-decor { position: absolute; inset: 0; }
  .back-info { position: absolute; left: 40px; top: 118px; }
  .back-info .wordmark { font-size: 32px; display: block; margin-bottom: 12px; }
  .accent-bar {
    position: absolute; left: 0; top: 180px; bottom: 0;
    width: 8px; background: var(--brand-blue);
  }
  .holder-name {
    font-family: "Oswald", "Arial Narrow", sans-serif;
    font-weight: 600; font-size: 18px;
    color: var(--brand-blue); text-transform: uppercase; line-height: 1.1;
    margin-left: 30px;
  }
  .holder-role, .address, .contacts { margin-left: 48px; color: var(--brand-blue); font-size: 15px; }
  .holder-role { margin-bottom: 10px; }
  .address { line-height: 1.25; margin-bottom: 10px; }
  .contacts { list-style: none; margin-left: 44px; }
  .contacts li { display: flex; align-items: center; gap: 8px; line-height: 1.3; }
  .contacts svg { width: 13px; height: 13px; fill: var(--brand-blue); flex: none; }
</style>
</head>
<body>

<section class="card card--front" aria-label="Fronte">
  <div class="front-ring" aria-hidden="true"></div>
  <div class="front-brand">
    <span class="brand-dot" aria-hidden="true"></span>
    <span class="wordmark">pianoverde</span>
  </div>
  <div class="benefit-tag">Società Benefit</div>
  <div class="claim-line claim-line--one"></div>
  <div class="claim-line claim-line--two"></div>
  <div class="front-web">www.<strong>pianoverde</strong>.it</div>
</section>

<section class="card card--back" aria-label="Retro">
  <svg class="back-decor" viewBox="0 0 620 354" aria-hidden="true">
    <circle cx="490" cy="95" r="200" fill="var(--brand-blue)"/>
    <circle cx="478" cy="102" r="208" fill="none" stroke="var(--brand-blue)" stroke-width="3"/>
  </svg>
  <div class="accent-bar"></div>
  <div class="back-info">
    <span class="wordmark">pianoverde</span>
    <div class="holder-name">Luca Ferentino</div>
    <div class="holder-role">Co-fondatore</div>
    <div class="address">Via Lucerna, 7<br>21047 - Saronno (VA)</div>
    <ul class="contacts">
      <li><svg viewBox="0 0 16 16"><path d="M4 1h8v14H4zM5.5 2.5v9h5v-9zM7 12.5h2v1H7z" fill-rule="evenodd"/></svg>+39 348 915 2074</li>
      <li><svg viewBox="0 0 16 16"><path d="M3 1l3 0 1 4-2 1c1 2 2 3 4 4l1-2 4 1v3c0 1-1 2-2 2C6 14 2 10 1 3c0-1 1-2 2-2z"/></svg>+39 348 915 2074</li>
      <li><svg viewBox="0 0 16 16"><path d="M4 2h8v4H4zM2 7h12v6h-2v2H4v-2H2zM5 11v3h6v-3z" fill-rule="evenodd"/></svg>+39 348 915 2074</li>
      <li><svg viewBox="0 0 16 16"><path d="M1 3h14v10H1zM2.5 4.5v.4L8 9l5.5-4.1v-.4zM2.5 6.7v4.8h11V6.7L8 10.8z" fill-rule="evenodd"/></svg>luca@pianoverde.it</li>
    </ul>
  </div>
</section>

</body>
</html>
```